New Zealand Marlborough Sauvignon Blanc wine packaging design

We need packaging design for our new wine brand, Dunmore Hale. The wine is a New Zealand Marlborough Sauvignon Blanc. We would like the packaging will portray elegance and style with an understated label. We are looking for a label that portrays the elegance of the French Riviera. The label should be round or pill shaped.
Updates

Industry/Entity Type

Wine

Font styles to use
Serif
Sans Serif

Requirements
Must have
• The words in order of importance: Dunmore Hale, Sauvignon Blanc, Marlborough, New Zealand. It should be fit to the bottle posted in the links
Nice to have
• a pill shape or circular shape
Should not have
• Illustrations of wine bottles, wine glasses, or grapes

```html
<!DOCTYPE html>
<html lang="en">
<head>
<meta charset="utf-8">
<title>Dunmore Hale Sauvignon Blanc Label</title>
<link href="https://fonts.googleapis.com/css2?family=Italiana&family=Inter:wght@400&display=swap" rel="stylesheet">
<style>
  :root {
    --canvas-bg: #000000;
    --label-ink: #ffffff;
    --sky-top: #9a9a9a;
    --sky-light: #e4e4e4;
    --horizon: #7a7a7a;
    --water-light: #dcdcdc;
    --water-mid: #b4b4b4;
    --foliage-dark: #1e1e1e;
  }
  html, body {
    margin: 0;
    padding: 0;
    width: 705px;
    height: 1200px;
    overflow: hidden;
    background: var(--canvas-bg);
  }
  .label-canvas {
    display: block;
    width: 705px;
    height: 1200px;
    will-change: transform;
    transform: translateZ(0);
  }
  .label-canvas text {
    -webkit-font-smoothing: antialiased;
    -moz-osx-font-smoothing: grayscale;
    text-rendering: geometricPrecision;
  }
  .label-name,
  .label-variety {
    font-family: "Italiana", serif;
    fill: var(--label-ink);
    letter-spacing: 2px;
  }
  .label-name { font-size: 38px; }
  .label-variety { font-size: 30px; }
  .label-region {
    font-family: "Inter", sans-serif;
    font-size: 14px;
    letter-spacing: 1px;
    fill: var(--label-ink);
  }
</style>
</head>
<body>
<svg class="label-canvas" viewBox="0 0 705 1200" xmlns="http://www.w3.org/2000/svg">
  <defs>
    <linearGradient id="sceneTone" x1="0" y1="0" x2="0" y2="1">
      <stop offset="0" stop-color="var(--sky-top)"/>
      <stop offset="0.18" stop-color="var(--sky-light)"/>
      <stop offset="0.3" stop-color="var(--sky-light)"/>
      <stop offset="0.36" stop-color="var(--horizon)"/>
      <stop offset="0.42" stop-color="var(--water-light)"/>
      <stop offset="0.7" stop-color="var(--water-mid)"/>
      <stop offset="1" stop-color="var(--horizon)"/>
    </linearGradient>
    <radialGradient id="foliageShade" cx="0.78" cy="0.82" r="0.55">
      <stop offset="0" stop-color="var(--foliage-dark)" stop-opacity="0.95"/>
      <stop offset="0.55" stop-color="var(--foliage-dark)" stop-opacity="0.55"/>
      <stop offset="1" stop-color="var(--foliage-dark)" stop-opacity="0"/>
    </radialGradient>
    <radialGradient id="shoreShade" cx="0.12" cy="0.36" r="0.3">
      <stop offset="0" stop-color="var(--foliage-dark)" stop-opacity="0.45"/>
      <stop offset="1" stop-color="var(--foliage-dark)" stop-opacity="0"/>
    </radialGradient>
    <path id="nameArc" d="M 160 600 A 192 212 0 0 1 544 600"/>
    <path id="varietyArc" d="M 140 600 A 212 234 0 0 0 564 600"/>
  </defs>

  <g class="label-illustration" role="img" aria-label="Pencil-style monochrome illustration of a Riviera harbour with seaside houses, sailboats on calm water and palm fronds in the foreground">
    <ellipse cx="352" cy="600" rx="160" ry="190" fill="url(#sceneTone)"/>
    <ellipse cx="352" cy="600" rx="160" ry="190" fill="url(#shoreShade)"/>
    <ellipse cx="352" cy="600" rx="160" ry="190" fill="url(#foliageShade)"/>
  </g>

  <text class="label-name">
    <textPath href="#nameArc" startOffset="50%" text-anchor="middle">DUNMORE HALE</textPath>
  </text>

  <text class="label-variety">
    <textPath href="#varietyArc" startOffset="50%" text-anchor="middle">SAUVIGNON BLANC</textPath>
  </text>

  <text class="label-region" transform="translate(182 600) rotate(-90)" text-anchor="middle">MARLBOROUGH</text>
  <text class="label-region" transform="translate(524 600) rotate(90)" text-anchor="middle">NEW ZEALAND</text>
</svg>
</body>
</html>
```